Flyer-Design für Initiativbewerbung
Zielgruppe
Wir sind ein Buchhaltungsbüro. Mit diesem Flyer möchten wir uns bei Steuerberater als freier Mitarbeiter bewerben als initiativ Bewerbung! Ich lade Bilder von mir selbst mit hoch um so noch persönlicher zu werden. Die Bilder können gerne bearbeitet werden und Ausschnitte gezogen werden. Es soll sehr persönlich rüber kommen
Aufgabenstellung
Flyer sollte Din A Lang sein als Endformat, also gerne auch mehrseitig und max. 20 g haben
Sie können auch Textpassagen duplizieren und auf eine Vorderseite etc machen.
Es soll persönlich wirken obwohl es ein Werbeversand. Anbei auch das Logo unserer Firma.
Ich bin auch offen das Logo in Schwarz weiß darzustellen um so vom Blau wegzukommen.
Ich lasse mich gerne überraschen.
Text
Initiativ Bewerbung freier Mitarbeiter für Ihre Kanzlei
Sehr geehrte Damen und Herren,
gerne bewerben wir uns als freier Mitarbeiter im Rahmen des

```html
<!DOCTYPE html>
<html lang="de">
<head>
<meta charset="utf-8">
<title>Initiativ Bewerbung – Flyer DIN lang</title>
<link href="https://fonts.googleapis.com/css2?family=Barlow:wght@400;500&display=swap" rel="stylesheet">
<style>
  :root {
    --page: #ffffff;
    --band-grey: #d3d3d3;
    --paper-white: #ffffff;
    --brand-blue: #1760b8;
    --ink: #2a2a2a;
    --ink-soft: #3c3c3c;
    --on-blue: #ffffff;
    --photo-light: #c9c9c9;
    --photo-dark: #5a5a5a;
  }
  * { margin: 0; padding: 0; box-sizing: border-box; }
  html, body { width: 1200px; height: 473px; overflow: hidden; background: var(--page); }
  body { font-family: "Barlow", Arial, sans-serif; color: var(--ink); position: relative; }

  .panel {
    position: absolute;
    top: 24px;
    width: 200px;
    height: 424px;
    background: var(--paper-white);
    box-shadow: 2px 3px 6px rgba(0,0,0,0.25);
    overflow: hidden;
  }
  .panel--front { left: 745px; }
  .panel--back { left: 967px; }

  .abs { position: absolute; left: 0; width: 100%; }

  /* Front */
  .title-band { top: 21px; height: 64px; background: var(--band-grey); text-align: center; }
  .title-band__headline {
    position: absolute; top: 19px; width: 100%;
    font-size: 11px; letter-spacing: 3.4px; color: var(--paper-white); font-weight: 500;
  }
  .title-band__sub {
    position: absolute; top: 38px; width: 100%;
    font-size: 4.4px; letter-spacing: 2px; color: var(--ink); font-weight: 500;
  }
  .portrait {
    top: 85px; height: 199px;
    background: linear-gradient(100deg, var(--photo-light) 0%, #8d8d8d 45%, var(--photo-dark) 60%, #e6e6e6 100%);
  }
  .brand-band { top: 308px; height: 116px; background: var(--brand-blue); }
  .brand {
    position: absolute; top: 34px; width: 100%;
    text-align: center; color: var(--on-blue);
  }
  .brand__square { display: block; width: 16px; height: 16px; margin: 0 auto 7px; background: var(--on-blue); }
  .brand__name { display: block; font-size: 15px; letter-spacing: 0.8px; font-weight: 400; line-height: 1.1; }

  /* Back */
  .letter-area { top: 0; height: 303px; background: var(--band-grey); }
  .line {
    position: absolute; width: 100%; text-align: center;
    font-size: 6.4px; color: var(--ink); line-height: 1; white-space: nowrap;
  }
  .services {
    position: absolute; left: 20px; right: 20px; top: 116px; height: 60px;
    background: var(--paper-white);
  }
  .services .line { font-size: 5.2px; letter-spacing: 0.5px; color: var(--ink-soft); }
  .signature {
    position: absolute; left: 62px; width: 76px; top: 257px; height: 23px;
    background: linear-gradient(90deg, rgba(23,96,184,0.08), rgba(23,96,184,0.18), rgba(23,96,184,0.08));
    border-radius: 3px;
  }
  .contact-band { top: 321px; height: 103px; background: var(--brand-blue); color: var(--on-blue); }
  .contact-band .line { color: var(--on-blue); font-size: 6.4px; }
  .contact-band .contact__label { letter-spacing: 2.1px; font-weight: 500; }
  .icon { display: inline-block; vertical-align: -1px; margin-right: 3px; }
</style>
</head>
<body>

<section class="panel panel--front">
  <div class="abs title-band">
    <div class="title-band__headline">INITIATIV BEWERBUNG</div>
    <div class="title-band__sub">FREIER MITARBEITER FÜR IHRE KANZLEI</div>
  </div>
  <div class="abs portrait" role="img" aria-label="Schwarz-Weiß-Porträt des Inhabers am Schreibtisch"></div>
  <div class="abs brand-band">
    <div class="brand">
      <span class="brand__square"></span>
      <span class="brand__name">Lindhof GmbH</span>
    </div>
  </div>
</section>

<section class="panel panel--back">
  <div class="abs letter-area">
    <p class="line" style="top:25px">Sehr geehrte Damen und Herren,</p>
    <p class="line" style="top:50px">gerne bewerben wir uns als freier Mitarbeiter im</p>
    <p class="line" style="top:63px">Rahmen des § 17 BOStB für Ihre Kanzlei.</p>
    <p class="line" style="top:88px">Gerne übernehmen wir für Sie im Rahmen der</p>
    <p class="line" style="top:101px">freien Mitarbeiter:</p>
    <div class="services">
      <p class="line" style="top:10px">FINANZBUCHHALTUNG</p>
      <p class="line" style="top:22px">LOHNBUCHHALTUNG (AUCH BAULOHN)</p>
      <p class="line" style="top:34px">JAHRESABSCHLUSS</p>
      <p class="line" style="top:45px">STEUERERKLÄRUNGEN</p>
    </div>
    <p class="line" style="top:185px">Fachliche Erfahrungen bestehen seit über 20</p>
    <p class="line" style="top:198px">Jahren. Die Tätigkeit auf diversen branchenübli-</p>
    <p class="line" style="top:211px">chen Abrechnungsprogrammen ist uns vertraut.</p>
    <p class="line" style="top:237px">Mit freundlichen Grüßen</p>
    <div class="signature" role="img" aria-label="Handschriftliche Unterschrift von Jonas Keller"></div>
  </div>
  <div class="abs contact-band">
    <p class="line contact__label" style="top:18px">KONTAKTDATEN:</p>
    <p class="line" style="top:31px">Lindhof GmbH</p>
    <p class="line" style="top:44px">Lindenstraße 12</p>
    <p class="line" style="top:57px">70123 Musterstadt</p>
    <p class="line" style="top:70px">
      <svg class="icon" width="5" height="6" viewBox="0 0 5 6" aria-hidden="true"><path d="M1 0.5 Q4 3 1 5.5" stroke="#fff" stroke-width="1.2" fill="none"/></svg>0711/1234567
    </p>
    <p class="line" style="top:83px">
      <svg class="icon" width="8" height="6" viewBox="0 0 8 6" aria-hidden="true"><rect x="0.4" y="0.4" width="7.2" height="5.2" stroke="#fff" stroke-width="0.7" fill="none"/><path d="M0.4 0.4 L4 3.4 L7.6 0.4" stroke="#fff" stroke-width="0.7" fill="none"/></svg>info@lindhof-beispiel.de
    </p>
  </div>
</section>

</body>
</html>
```